BUSINESS CARD, LETTERHEAD ENVELOPES FOR VIDEO PRODUCTION COMPANY
NO SUBTITLE NECESSARY - PLEASE UPLOAD WINNING LOGO FOR ME!!!
Simple
Owen Marsh
Founder
Corporate Offices: 700 Central Expressway  Suite 550 Brookvale, TX 75094​
555.01.BLOOM (555.012.5666)
owen@lumaharbor.com
www.lumaharbor.com
Looking for a very clean, simple design that shows off the logo...GOOD LUCK!!!
OUR SERVICES & AREAS OF EXPERTISE Corporate Trainings & Events Individual Spotlights Client Testimonials Music Venues & City Festivals Legal & Court Depositions Non-Profit Fundraisers

```html
<!DOCTYPE html>
<html lang="en">
<head>
<meta charset="utf-8">
<title>Luma Harbor Stationery</title>
<link href="https://fonts.googleapis.com/css2?family=Montserrat:wght@400;600&family=Open+Sans:wght@400;600&display=swap" rel="stylesheet">
<style>
  :root {
    --teal: #12978a;
    --ink: #1f2326;
    --paper: #ffffff;
    --muted: #6d7378;
    --body-text: #4a4f53;
    --stage: #e6e8ea;
  }
  * { box-sizing: border-box; margin: 0; padding: 0; }
  html, body { width: 1200px; height: 862px; overflow: hidden; }
  body {
    background: var(--stage);
    font-family: "Open Sans", Arial, sans-serif;
    color: var(--ink);
    position: relative;
  }
  .brand {
    display: flex; align-items: center; gap: 8px;
    font-family: "Montserrat", Arial, sans-serif;
    font-weight: 600; color: var(--teal);
    white-space: nowrap;
  }
  .brand-square { background: var(--teal); display: block; flex: none; }

  /* Envelope */
  .envelope {
    position: absolute; left: 50px; top: 50px;
    width: 600px; height: 280px;
    background: var(--paper);
    box-shadow: 0 6px 18px rgba(0,0,0,.15);
    overflow: hidden;
  }
  .envelope-band {
    position: absolute; right: 0; top: 0; width: 190px; height: 100%;
  }
  .envelope .brand { position: absolute; left: 36px; top: 36px; font-size: 22px; }
  .envelope .brand-square { width: 26px; height: 26px; }
  .envelope-return {
    position: absolute; left: 36px; top: 84px;
    font-size: 10px; line-height: 1.6; color: var(--muted);
  }

  /* Business cards */
  .card {
    position: absolute; width: 300px; height: 170px;
    background: var(--paper);
    box-shadow: 0 6px 14px rgba(0,0,0,.15);
    overflow: hidden;
  }
  .card-front { left: 50px; top: 380px; }
  .card-front .card-band {
    position: absolute; left: 0; bottom: 0; width: 100%; height: 42px;
    background: var(--teal);
  }
  .card-front .brand {
    position: absolute; left: 0; right: 0; top: 52px;
    justify-content: center; font-size: 22px;
  }
  .card-front .brand-square { width: 24px; height: 24px; }

  .card-back { left: 50px; top: 590px; }
  .card-back .card-band {
    position: absolute; left: 0; top: 0; width: 92px; height: 100%;
    background: var(--ink);
  }
  .card-back .card-band::after {
    content: ""; position: absolute; right: 0; top: 0; width: 8px; height: 100%;
    background: var(--teal);
  }
  .card-back .card-details { position: absolute; left: 112px; top: 22px; right: 12px; }
  .card-name { font-family: "Montserrat", Arial, sans-serif; font-weight: 600; font-size: 15px; }
  .card-role { font-size: 10px; color: var(--teal); margin-bottom: 10px; }
  .card-contact { font-size: 8.5px; line-height: 1.65; color: var(--muted); }

  /* Letterhead */
  .letterhead {
    position: absolute; left: 700px; top: 50px;
    width: 450px; height: 636px;
    background: var(--paper);
    box-shadow: 0 6px 18px rgba(0,0,0,.15);
    overflow: hidden;
  }
  .letterhead-header {
    display: flex; justify-content: flex-end;
    padding: 40px 44px 0;
  }
  .letterhead .brand { font-size: 24px; }
  .letterhead .brand-square { width: 28px; height: 28px; }
  .letterhead-body {
    padding: 60px 44px 0;
    font-size: 10px; line-height: 1.75; color: var(--body-text);
  }
  .letterhead-body p { margin-bottom: 12px; }
  .letterhead-sign { margin-top: 24px; }
  .letterhead-footer {
    position: absolute; left: 44px; right: 44px; bottom: 44px;
    font-size: 8.5px; line-height: 1.6; color: var(--muted);
  }
  .letterhead-band {
    position: absolute; left: 0; bottom: 0; width: 100%; height: 20px;
    background: var(--teal);
  }
</style>
</head>
<body>

  <section class="envelope" aria-label="Envelope">
    <svg class="envelope-band" viewBox="0 0 190 280" preserveAspectRatio="none" aria-hidden="true">
      <polygon points="80,0 190,0 190,280 0,280" fill="#1f2326"/>
      <polygon points="150,0 190,0 190,280 110,280" fill="#12978a"/>
    </svg>
    <div class="brand"><span class="brand-square"></span>Luma Harbor</div>
    <div class="envelope-return">
      418 Harlow Parkway Suite 220<br>
      Brookvale, TX 75094<br>
      www.lumaharbor.com
    </div>
  </section>

  <section class="card card-front" aria-label="Business card front">
    <div class="brand"><span class="brand-square"></span>Luma Harbor</div>
    <div class="card-band"></div>
  </section>

  <section class="card card-back" aria-label="Business card back">
    <div class="card-band"></div>
    <div class="card-details">
      <div class="card-name">Owen Marsh</div>
      <div class="card-role">Founder</div>
      <div class="card-contact">
        418 Harlow Parkway Suite 220<br>
        Brookvale, TX 75094<br>
        555.01.BLOOM (555.012.5666)<br>
        owen@lumaharbor.com<br>
        www.lumaharbor.com
      </div>
    </div>
  </section>

  <section class="letterhead" aria-label="Letterhead">
    <header class="letterhead-header">
      <div class="brand"><span class="brand-square"></span>Luma Harbor</div>
    </header>
    <div class="letterhead-body">
      <p>Dear client, thank you for choosing our studio for your next production. We plan, shoot and edit each project with care, from the first call to final delivery.</p>
      <p>Our team covers corporate events, client testimonials, music venues and city festivals, and we keep every step clear and on schedule.</p>
      <p>Please review the enclosed proposal and reach out with any questions.</p>
      <p class="letterhead-sign">Sincerely,<br><strong>Owen Marsh</strong><br>Founder</p>
    </div>
    <footer class="letterhead-footer">
      Corporate Offices: 418 Harlow Parkway Suite 220 Brookvale, TX 75094<br>
      555.01.BLOOM (555.012.5666) &nbsp;·&nbsp; owen@lumaharbor.com &nbsp;·&nbsp; www.lumaharbor.com
    </footer>
    <div class="letterhead-band"></div>
  </section>

</body>
</html>
```